Business Card Design for a Software Startup

We'd like to have a business card design. We already have a logo. Basically what we need is a clean design with name, address, cellphone and phone numbers, e-mail and web site address (front) and a space on the back with our logo with the company name on the right side and some texts on the bottom.
We are a development and consulting company in Brazil with highly qualified team of professionals in Java, iOS and Android development and consulting.

Target Market(s)

CIO, IT managers of mid to big size companies

Industry/Entity Type

Business

```html
<!DOCTYPE html>
<html lang="en">
<head>
<meta charset="UTF-8">
<title>Vantro Business Card</title>
<link href="https://fonts.googleapis.com/css2?family=Cabin:wght@400;500;600&display=swap" rel="stylesheet">
<style>
  :root {
    --stage: #d9dadc;
    --card-white: #ffffff;
    --navy: #123a66;
    --deep-blue: #0f3566;
    --mid-blue: #1f5fa3;
    --ray-blue: #3d7fc4;
    --accent-blue: #2aa3e0;
    --ink: #2b2b2b;
    --soft-grey: #eef1f4;
  }
  * { margin: 0; padding: 0; box-sizing: border-box; }
  html, body {
    width: 1200px; height: 900px; overflow: hidden;
    background: var(--stage);
    font-family: "Cabin", "Gill Sans", sans-serif;
  }
  .canvas { position: relative; width: 1200px; height: 900px; }
  .card {
    position: absolute; left: 320px; width: 560px; height: 320px;
    box-shadow: 0 6px 18px rgba(0,0,0,0.18);
    overflow: hidden;
  }

  /* Back face */
  .card-back {
    top: 100px;
    background: linear-gradient(135deg, var(--mid-blue) 0%, var(--deep-blue) 55%, #0c2b55 100%);
    color: #fff;
  }
  .back-rays {
    position: absolute; inset: 0;
    background: linear-gradient(160deg, rgba(80,150,220,0.35) 0%, rgba(80,150,220,0) 55%);
  }
  .back-band {
    position: absolute; left: -80px; width: 420px; height: 26px;
    background: var(--ray-blue); opacity: 0.22;
    transform-origin: left center;
  }
  .back-band.band-one { top: 150px; transform: rotate(-28deg); }
  .back-band.band-two { top: 230px; transform: rotate(-22deg); height: 18px; }
  .back-brand {
    position: absolute; left: 290px; top: 128px;
    display: flex; align-items: center; gap: 12px;
  }
  .back-brand .brand-square { width: 34px; height: 34px; background: #fff; }
  .back-brand .brand-name {
    font-size: 44px; font-weight: 500; letter-spacing: 1px; color: #fff; line-height: 1;
  }
  .back-tagline {
    position: absolute; left: 0; right: 0; bottom: 30px;
    text-align: center; font-size: 13px; letter-spacing: 0.6px;
  }

  /* Front face */
  .card-front {
    top: 480px;
    background: var(--card-white);
    color: var(--ink);
  }
  .front-wash {
    position: absolute; inset: 0;
    background: linear-gradient(160deg, var(--card-white) 30%, var(--soft-grey) 60%, var(--card-white) 85%);
  }
  .front-brand {
    position: absolute; left: 36px; top: 118px;
    display: flex; align-items: center; gap: 10px;
  }
  .front-brand .brand-square { width: 30px; height: 30px; background: var(--mid-blue); }
  .front-brand .brand-name {
    font-size: 40px; font-weight: 600; letter-spacing: 1px; color: var(--navy); line-height: 1;
  }
  .divider {
    position: absolute; left: 258px; top: 172px; width: 1px; height: 108px;
    background: var(--accent-blue);
  }
  .person { position: absolute; left: 280px; top: 46px; }
  .person-name {
    font-size: 22px; font-weight: 400; color: var(--accent-blue); letter-spacing: 0.5px; line-height: 1.2;
  }
  .person-title { font-size: 13px; margin-top: 2px; }
  .contact-list {
    position: absolute; left: 280px;
    display: grid; grid-template-columns: 48px auto; row-gap: 3px;
    font-size: 13px; line-height: 1.25;
  }
  .contact-list dt { color: var(--accent-blue); }
  .contact-list dd { color: var(--ink); }
  .phones { top: 118px; }
  .online { top: 184px; }
  .address {
    position: absolute; left: 280px; top: 240px;
    font-size: 13px; font-style: normal; line-height: 1.4;
  }
</style>
</head>
<body>
<main class="canvas">
  <section class="card card-back" aria-label="Card back">
    <div class="back-rays" role="img" aria-label="Soft diagonal light rays in lighter blue"></div>
    <span class="back-band band-one"></span>
    <span class="back-band band-two"></span>
    <div class="back-brand">
      <span class="brand-square"></span>
      <span class="brand-name">VANTRO</span>
    </div>
    <p class="back-tagline">JAVA • iOS • ANDROID • DEVELOPMENT &amp; CONSULTING</p>
  </section>

  <section class="card card-front" aria-label="Card front">
    <div class="front-wash" role="img" aria-label="Faint pale grey diagonal light bands"></div>
    <div class="front-brand">
      <span class="brand-square"></span>
      <span class="brand-name">VANTRO</span>
    </div>
    <div class="divider"></div>
    <div class="person">
      <h1 class="person-name">DANIEL MOREAU</h1>
      <p class="person-title">Managing Director</p>
    </div>
    <dl class="contact-list phones">
      <dt>Phone</dt><dd>555 310 42 18</dd>
      <dt>Cell</dt><dd>555 204 31 77</dd>
    </dl>
    <dl class="contact-list online">
      <dt>Email</dt><dd>info@vantro.com</dd>
      <dt>Web</dt><dd>www.vantro.com</dd>
    </dl>
    <address class="address">48 Harbor Lane<br>Lakeview, Ohio 44021</address>
  </section>
</main>
</body>
</html>
```